Wordpress Website Design/Launch for Aerial Drone Company

My company (Skyward Lens Reels) recently obtained NVB 333 clearance to fly drones for commercial use. I am a needing a very simple, but very visual & techy (icons/colors) look and feel website. aerial images of cities, solar farms, agriculture, buildings can be used since our services will focus on providing aerial video & photography for the following sectors:

- Real Estate Videos for commercial, industrial, retail, multi-family and residential, big focus on developers (new construction type projects. (main market)

- Agricultural videos

- Utilities (electrical line inspection, hydro dams, pipelines, sewage plants, solar farms, fracking operations.

- Hospitality (hotels, resorts)

- Retirement Communities

- Hospitals

- CONSERVATION, ENVIRONMENTAL REGULATION AND COMPLIANCE

- Disaster Relief

- Sporting Events / Festivals / Stadiums, Ballparks
- International availability

This It needs to be WordPress
Easily managed by my team on the backend (including: adding copy, uploading and changing videos and pictures)
Must have a blog
No social media now but needs to have plugins added so we can link when ready

The site should appeal to and have a call to action on every page: contact us via phone, contact form, and click the videos (will need to add) .

Right now I see only 5 pages:
Home (background flying videos through cities/over buildings on streets etc ??)
About Us
Services (see above service areas will need icons for each)
Our Work
Contact Us (needs to integrate into Kelvora CRM)
Blog

I am looking for the website to be designed, coded and launch on our hosting server (hostpalm).

Example of a website
http://www.gliderfoxstudios.example

** We do not have a logo so I would like to see whys you can be creative with our name. The website domain is www.skywardlensreels.example.

Target Market(s)

Target market will be:

Real Estate Market (Residential, Commercial, Industrial, developers)
Utilities (Oil companies, electric companies, natural gas companies)
Hospitals
Hotels & Resorts
Farmers (agricultural survey)
Cities & Municipals for aerial surveying/builiding inspections
Blue Harbor Aid / Disaster Relief
Sporting Events / Stadiums - football/Baseball / High School sports

Industry/Entity Type

It Company

Number of Pages Required

5+ page

Requirements
Must have
• Must be very visual
• Include custom icons for the target audience / services
• background video on the home page/ additional pages of flying through cities/streets/ by buildings/ over land / solar farms etc.
• Clean professional look / simple
Nice to have
• I am open to all ideas
• unique logo for our name "Skyward Lens Reels"

```html
<!DOCTYPE html>
<html lang="en">
<head>
<meta charset="utf-8">
<title>Skyward Lens Reels – Aerial Video &amp; Photography</title>
<link href="https://fonts.googleapis.com/css2?family=Open+Sans:ital,wght@0,400;0,600;0,700;1,700&family=Righteous&display=swap" rel="stylesheet">
<style>
:root{
  --blue:#1f7fd6;
  --blue-deep:#0f4f9e;
  --blue-dark:#0b3c7a;
  --blue-light:#3aa0f0;
  --ink:#1d2b3a;
  --text:#5b6470;
  --muted:#8a939e;
  --line:#dfe4ea;
  --bg-soft:#f3f6f9;
  --white:#ffffff;
}
*{box-sizing:border-box;margin:0;padding:0}
html,body{width:1200px;height:2840px;overflow:hidden}
body{font-family:"Open Sans",Arial,sans-serif;color:var(--text);background:var(--white);font-size:13px;line-height:1.6}
a{color:inherit;text-decoration:none}
.wrap{width:1056px;margin:0 auto;position:relative}

/* header */
.site-header{height:88px;background:var(--white);border-bottom:1px solid var(--line);position:relative}
.brand{position:absolute;left:72px;top:18px;display:flex;align-items:center;gap:12px}
.brand-mark{width:50px;height:50px;border-radius:50%;background:var(--blue)}
.brand-name{font-family:"Righteous",sans-serif;font-size:25px;line-height:1.05;color:var(--blue);width:150px}
.main-nav{position:absolute;left:396px;top:32px;display:flex;gap:30px;font-size:12px;font-weight:600;color:var(--ink);letter-spacing:.5px}
.main-nav a.active{color:var(--blue);border-bottom:2px solid var(--blue);padding-bottom:6px}
.header-cta{position:absolute;right:28px;top:0;width:136px;height:88px;background:var(--blue);color:var(--white);display:flex;align-items:center;justify-content:center;gap:8px;font-weight:700;line-height:1.1}
.header-cta small{display:block;font-size:10px;font-weight:600}
.header-cta span{font-size:19px}

/* hero */
.hero{height:552px;position:relative;background:linear-gradient(180deg,#9fb2c4 0%,#7d8f9f 40%,#5d6c78 75%,#4a5560 100%)}
.slider-arrow{position:absolute;top:250px;width:40px;height:40px;border-radius:50%;background:rgba(255,255,255,.85);display:flex;align-items:center;justify-content:center}
.slider-arrow.prev{left:20px}.slider-arrow.next{right:20px}

/* welcome */
.welcome{height:260px;text-align:center;padding-top:40px;background:linear-gradient(180deg,#fff 0%,#eef3f8 100%)}
.welcome-kicker{font-family:"Righteous",sans-serif;font-size:24px;color:var(--blue-dark)}
.welcome-title{font-family:"Righteous",sans-serif;font-size:46px;color:var(--blue);line-height:1.1;margin-bottom:14px}
.welcome p{width:800px;margin:0 auto;font-size:13px}

/* services */
.services{height:420px;background:#eef3f8;position:relative}
.services .slider-arrow{top:150px;background:none;width:24px}
.service-list{display:flex;justify-content:center;gap:50px;padding-top:10px}
.service-card{width:164px;height:386px;border-radius:82px;background:linear-gradient(180deg,var(--blue-light) 0%,var(--blue) 45%,var(--blue-deep) 100%);text-align:center;color:var(--white);padding:12px 14px 0;box-shadow:0 6px 14px rgba(15,79,158,.25)}
.service-icon{width:136px;height:136px;border-radius:50%;background:var(--white);display:flex;align-items:center;justify-content:center;margin-bottom:18px}
.service-card h3{font-size:15px;font-weight:700;margin-bottom:8px}
.service-card p{font-size:11px;line-height:1.5;margin-bottom:16px;color:#e4f0fb}
.btn-small{display:inline-block;background:var(--blue-dark);color:var(--white);font-size:10px;font-weight:700;padding:6px 14px;border-radius:14px}

/* video work */
.work{height:520px;padding-top:34px}
.work-grid{display:flex;gap:40px}
.work-item{width:325px}
.work-item h3{display:flex;align-items:center;gap:10px;font-size:18px;color:var(--ink);font-weight:700;margin-bottom:12px}
.video{height:200px;position:relative;margin-bottom:14px}
.video-bar{position:absolute;left:0;right:0;bottom:0;height:26px;background:rgba(0,0,0,.55);display:flex;align-items:center;gap:8px;padding:0 8px}
.video-progress{flex:1;height:4px;background:rgba(255,255,255,.4);border-radius:2px;position:relative}
.video-progress i{position:absolute;left:0;top:0;height:4px;width:35%;background:var(--blue-light);border-radius:2px}
.video-play{position:absolute;left:50%;top:45%;transform:translate(-50%,-50%);width:52px;height:52px;border-radius:50%;background:rgba(255,255,255,.85);display:flex;align-items:center;justify-content:center}
.work-item p{font-size:12px}
.center{text-align:center}
.btn{display:inline-block;background:var(--blue-deep);color:var(--white);font-size:12px;font-weight:700;padding:11px 22px;border-radius:3px;letter-spacing:.5px}
.work .btn{margin-top:30px}
.divider{display:block;margin:30px auto 0}

/* blog */
.blog{height:508px;padding-top:10px}
.section-title{font-family:"Righteous",sans-serif;font-size:32px;color:var(--ink);text-align:center;margin-bottom:22px}
.blog-grid{display:flex;gap:40px}
.blog-card{width:325px}
.blog-image{height:200px}
.blog-meta{height:30px;background:var(--blue);color:var(--white);display:flex;justify-content:space-between;align-items:center;padding:0 12px;font-size:11px;font-weight:600}
.blog-meta span{display:flex;align-items:center;gap:6px}
.blog-card h4{font-size:17px;color:var(--ink);font-weight:700;margin:14px 0 6px}
.blog-card p{font-size:12px;margin-bottom:6px}
.read-more{font-size:11px;color:var(--blue);text-decoration:underline}

/* newsletter */
.newsletter{height:72px;background:linear-gradient(90deg,var(--blue-dark),var(--blue-deep));color:var(--white)}
.newsletter .wrap{display:flex;align-items:center;height:72px;gap:16px}
.newsletter h5{font-size:19px;font-style:italic;font-weight:700;margin-right:auto}
.newsletter .field{width:230px;height:32px;background:var(--white);color:var(--muted);font-size:11px;padding:7px 10px}
.newsletter .btn{background:var(--blue-light);padding:8px 22px;font-size:11px}

/* footer */
.site-footer{height:296px;padding-top:30px;background:var(--white)}
.footer-grid{display:flex;gap:40px}
.footer-col h6{font-size:14px;color:var(--ink);font-weight:700;margin-bottom:12px}
.links{width:220px;list-style:none;font-size:12px;line-height:2}
.touch{width:250px}
.touch li{list-style:none;display:flex;gap:10px;font-size:12px;margin-bottom:12px;line-height:1.4}
.touch svg{flex:none}
.form{width:546px}
.form p{font-size:11px;margin-bottom:10px}
.form-grid{display:grid;grid-template-columns:1fr 1fr;gap:8px}
.input{height:30px;border:1px solid var(--line);font-size:11px;color:var(--muted);padding:6px 10px}
.textarea{grid-column:1 / 3;height:44px}
.submit{grid-column:1 / 3;height:30px;background:var(--blue);color:var(--white);font-size:12px;font-weight:700;text-align:center;line-height:30px}
.copyright{height:80px;background:var(--bg-soft);font-size:11px;color:var(--muted);padding-top:24px}
</style>
</head>
<body>

<header class="site-header">
  <a class="brand" href="#"><span class="brand-mark"></span><span class="brand-name">Skyward Lens Reels</span></a>
  <nav class="main-nav">
    <a class="active" href="#">HOME</a><a href="#">ABOUT</a><a href="#">SERVICES</a><a href="#">OUR WORK</a><a href="#">BLOG</a><a href="#">CONTACT</a>
  </nav>
  <a class="header-cta" href="#">
    <svg width="26" height="26" viewBox="0 0 26 26"><circle cx="13" cy="13" r="11" fill="none" stroke="#fff" stroke-width="2"/><path d="M10 8l8 5-8 5z" fill="#fff"/></svg>
    <div><small>CLICK THE</small><span>VIDEOS</span></div>
  </a>
</header>

<section class="hero" role="img" aria-label="Aerial photograph of a city with a river, bridges and dense buildings">
  <span class="slider-arrow prev"><svg width="14" height="14" viewBox="0 0 14 14"><path d="M9 2L4 7l5 5" fill="none" stroke="#1d2b3a" stroke-width="2"/></svg></span>
  <span class="slider-arrow next"><svg width="14" height="14" viewBox="0 0 14 14"><path d="M5 2l5 5-5 5" fill="none" stroke="#1d2b3a" stroke-width="2"/></svg></span>
</section>

<section class="welcome">
  <div class="welcome-kicker">Welcome to</div>
  <h1 class="welcome-title">Skyward Lens Reels</h1>
  <p>Lorem ipsum dolor sit amet, consectetuer adipiscing elit, sed diam nonummy nibh euismod tincidunt ut laoreet dolore magna aliquam erat volutpat. Ut wisi enim ad minim veniam, quis nostrud exerci tation ullamcorper suscipit lobortis nisl ut aliquip ex ea commodo consequat. Duis autem vel eum iriure dolor in hendrerit in vulputate velit esse molestie consequat, vel illum dolore eu feugiat nulla facilisis at vero.</p>
</section>

<section class="services">
  <span class="slider-arrow prev"><svg width="16" height="30" viewBox="0 0 16 30"><path d="M13 2L3 15l10 13" fill="none" stroke="#0f4f9e" stroke-width="2"/></svg></span>
  <span class="slider-arrow next"><svg width="16" height="30" viewBox="0 0 16 30"><path d="M3 2l10 13L3 28" fill="none" stroke="#0f4f9e" stroke-width="2"/></svg></span>
  <div class="service-list">
    <article class="service-card">
      <div class="service-icon"><svg width="70" height="70" viewBox="0 0 70 70" fill="#1f7fd6"><rect x="10" y="22" width="18" height="42"/><rect x="32" y="8" width="20" height="56"/><rect x="54" y="34" width="10" height="30"/></svg></div>
      <h3>Real Estate</h3><p>Lorem ipsum dolor sit amet, consectetuer adipiscing elit, sed diam nonummy.</p><a class="btn-small" href="#">READ MORE</a>
    </article>
    <article class="service-card">
      <div class="service-icon"><svg width="70" height="70" viewBox="0 0 70 70" fill="#1f7fd6"><rect x="8" y="56" width="54" height="6"/><path d="M14 56V36l12-10 12 10v20z"/><circle cx="50" cy="20" r="8"/></svg></div>
      <h3>Agricultural</h3><p>Lorem ipsum dolor sit amet, consectetuer adipiscing elit, sed diam nonummy.</p><a class="btn-small" href="#">READ MORE</a>
    </article>
    <article class="service-card">
      <div class="service-icon"><svg width="70" height="70" viewBox="0 0 70 70" fill="none" stroke="#1f7fd6" stroke-width="4"><path d="M35 6L20 64M35 6l15 58M14 22h42M18 38h34"/></svg></div>
      <h3>Utilities</h3><p>Lorem ipsum dolor sit amet, consectetuer adipiscing elit, sed diam nonummy.</p><a class="btn-small" href="#">READ MORE</a>
    </article>
    <article class="service-card">
      <div class="service-icon"><svg width="70" height="70" viewBox="0 0 70 70" fill="#1f7fd6"><path d="M8 30a27 22 0 0 1 54 0z"/><rect x="33" y="30" width="4" height="30"/><rect x="14" y="60" width="42" height="4"/></svg></div>
      <h3>Hospitality</h3><p>Lorem ipsum dolor sit amet, consectetuer adipiscing elit, sed diam nonummy.</p><a class="btn-small" href="#">READ MORE</a>
    </article>
    <article class="service-card">
      <div class="service-icon"><svg width="70" height="70" viewBox="0 0 70 70" fill="#1f7fd6"><path d="M35 8l7 16 17 2-13 12 4 17-15-9-15 9 4-17-13-12 17-2z"/></svg></div>
      <h3>Festivals</h3><p>Lorem ipsum dolor sit amet, consectetuer adipiscing elit, sed diam nonummy.</p><a class="btn-small" href="#">READ MORE</a>
    </article>
  </div>
</section>

<section class="work">
  <div class="wrap">
    <div class="work-grid">
      <article class="work-item">
        <h3><svg width="24" height="24" viewBox="0 0 24 24" fill="#1d2b3a"><rect x="2" y="8" width="8" height="14"/><rect x="12" y="2" width="10" height="20"/></svg>Real Estate</h3>
        <div class="video" role="img" aria-label="Aerial video of a residential neighbourhood" style="background:linear-gradient(160deg,#6f8a6a,#9aa58f 50%,#c9c3b0)">
          <span class="video-play"><svg width="18" height="18" viewBox="0 0 18 18"><path d="M4 2l12 7-12 7z" fill="#1f7fd6"/></svg></span>
          <div class="video-bar"><svg width="10" height="10" viewBox="0 0 10 10"><path d="M1 0l9 5-9 5z" fill="#fff"/></svg><span class="video-progress"><i></i></span></div>
        </div>
        <p>Lorem ipsum dolor sit amet consectetuer adipiscing elit, sed diam nonummy nibh euismod tincidunt ut laoreet dolore magna aliquam erat volutpat.</p>
      </article>
      <article class="work-item">
        <h3><svg width="24" height="24" viewBox="0 0 24 24" fill="#1d2b3a"><path d="M2 22V12l8-6 8 6v10z"/><circle cx="20" cy="5" r="3"/></svg>Agricultural</h3>
        <div class="video" role="img" aria-label="Aerial video of farm fields and greenhouses" style="background:linear-gradient(160deg,#5d7a48,#8fa66a 50%,#c8cdb5)">
          <span class="video-play"><svg width="18" height="18" viewBox="0 0 18 18"><path d="M4 2l12 7-12 7z" fill="#1f7fd6"/></svg></span>
          <div class="video-bar"><svg width="10" height="10" viewBox="0 0 10 10"><path d="M1 0l9 5-9 5z" fill="#fff"/></svg><span class="video-progress"><i></i></span></div>
        </div>
        <p>Lorem ipsum dolor sit amet consectetuer adipiscing elit, sed diam nonummy nibh euismod tincidunt ut laoreet dolore magna aliquam erat volutpat.</p>
      </article>
      <article class="work-item">
        <h3><svg width="24" height="24" viewBox="0 0 24 24" fill="none" stroke="#1d2b3a" stroke-width="2"><path d="M12 2L6 22M12 2l6 20M4 8h16M6 14h12"/></svg>Utilities</h3>
        <div class="video" role="img" aria-label="Aerial video of a solar farm among green hills" style="background:linear-gradient(160deg,#4f7d4a,#9fb8c8 55%,#dfe6ea)">
          <span class="video-play"><svg width="18" height="18" viewBox="0 0 18 18"><path d="M4 2l12 7-12 7z" fill="#1f7fd6"/></svg></span>
          <div class="video-bar"><svg width="10" height="10" viewBox="0 0 10 10"><path d="M1 0l9 5-9 5z" fill="#fff"/></svg><span class="video-progress"><i></i></span></div>
        </div>
        <p>Lorem ipsum dolor sit amet consectetuer adipiscing elit, sed diam nonummy nibh euismod tincidunt ut laoreet dolore magna aliquam erat volutpat.</p>
      </article>
    </div>
    <div class="center"><a class="btn" href="#">MORE VIDEOS</a></div>
    <svg class="divider" width="22" height="22" viewBox="0 0 22 22"><path d="M4 4l14 14M18 4L4 18" stroke="#1f7fd6" stroke-width="3"/></svg>
  </div>
</section>

<section class="blog">
  <div class="wrap">
    <h2 class="section-title">Latest Blog</h2>
    <div class="blog-grid">
      <article class="blog-card">
        <div class="blog-image" role="img" aria-label="Aerial view of city towers and a park" style="background:linear-gradient(160deg,#6c8a9e,#9fb49a 60%,#c9d1c4)"></div>
        <div class="blog-meta"><span><svg width="12" height="12" viewBox="0 0 12 12"><rect x="1" y="2" width="10" height="9" fill="none" stroke="#fff"/><path d="M1 5h10" stroke="#fff"/></svg>25 Jun 2015</span><span><svg width="12" height="12" viewBox="0 0 12 12"><path d="M1 1h10v7H5l-3 3V8H1z" fill="#fff"/></svg>24 Comments</span></div>
        <h4>Lorem Ipsum dolor sit amet</h4>
        <p>Lorem ipsum dolor sit amet consectetuer adipiscing elit, sed diam nonummy nibh euismod tincidunt ut laoreet dolore magna aliquam erat volutpat.</p>
        <a class="read-more" href="#">Read More</a>
      </article>
      <article class="blog-card">
        <div class="blog-image" role="img" aria-label="Aerial view of a solar farm beside a stadium" style="background:linear-gradient(160deg,#5d7f55,#8ea28a 55%,#b8c1c8)"></div>
        <div class="blog-meta"><span><svg width="12" height="12" viewBox="0 0 12 12"><rect x="1" y="2" width="10" height="9" fill="none" stroke="#fff"/><path d="M1 5h10" stroke="#fff"/></svg>25 Jun 2015</span><span><svg width="12" height="12" viewBox="0 0 12 12"><path d="M1 1h10v7H5l-3 3V8H1z" fill="#fff"/></svg>24 Comments</span></div>
        <h4>Lorem Ipsum dolor sit amet</h4>
        <p>Lorem ipsum dolor sit amet consectetuer adipiscing elit, sed diam nonummy nibh euismod tincidunt ut laoreet dolore magna aliquam erat volutpat.</p>
        <a class="read-more" href="#">Read More</a>
      </article>
      <article class="blog-card">
        <div class="blog-image" role="img" aria-label="Aerial view of a town at sunset" style="background:linear-gradient(160deg,#3f5a3a,#8a8a5c 55%,#d3b27a)"></div>
        <div class="blog-meta"><span><svg width="12" height="12" viewBox="0 0 12 12"><rect x="1" y="2" width="10" height="9" fill="none" stroke="#fff"/><path d="M1 5h10" stroke="#fff"/></svg>25 Jun 2015</span><span><svg width="12" height="12" viewBox="0 0 12 12"><path d="M1 1h10v7H5l-3 3V8H1z" fill="#fff"/></svg>24 Comments</span></div>
        <h4>Lorem Ipsum dolor sit amet</h4>
        <p>Lorem ipsum dolor sit amet consectetuer adipiscing elit, sed diam nonummy nibh euismod tincidunt ut laoreet dolore magna aliquam erat volutpat.</p>
        <a class="read-more" href="#">Read More</a>
      </article>
    </div>
  </div>
</section>

<section class="newsletter">
  <div class="wrap">
    <svg width="40" height="26" viewBox="0 0 40 26"><path d="M2 4l16 10L36 2 28 24l-8-6-4 6v-8z" fill="none" stroke="#fff" stroke-width="2"/></svg>
    <h5>Subscribe Our Newsletter!</h5>
    <div class="field">Enter Your Name</div>
    <div class="field">Enter Your Email</div>
    <a class="btn" href="#">SUBSCRIBE</a>
  </div>
</section>

<footer class="site-footer">
  <div class="wrap footer-grid">
    <div class="footer-col">
      <h6>Quick Links</h6>
      <ul class="links"><li>Home</li><li>About</li><li>Services</li><li>Our Work</li><li>Blog</li><li>Contact</li></ul>
    </div>
    <div class="footer-col touch">
      <h6>Get in Touch</h6>
      <ul>
        <li><svg width="16" height="18" viewBox="0 0 16 18"><path d="M8 1a6 6 0 0 1 6 6c0 5-6 10-6 10S2 12 2 7a6 6 0 0 1 6-6z" fill="#1f7fd6"/><circle cx="8" cy="7" r="2" fill="#fff"/></svg><span>1234, Harbor Crest Drive,<br>Fenwick, FL 10000</span></li>
        <li><svg width="16" height="16" viewBox="0 0 16 16"><path d="M3 1l3 1 1 3-2 2a9 9 0 0 0 4 4l2-2 3 1 1 3-2 2C7 15 1 9 1 3z" fill="#1f7fd6"/></svg><span>Phone<br>(888) 888-8888</span></li>
        <li><svg width="16" height="14" viewBox="0 0 16 14"><rect x="1" y="2" width="14" height="10" fill="#1f7fd6"/><path d="M1 2l7 6 7-6" fill="none" stroke="#fff"/></svg><span>Email<br>info@skywardlensreels.example</span></li>
      </ul>
    </div>
    <div class="footer-col form">
      <h6>Contact Form</h6>
      <p>All fields marked are required. Contact us today.</p>
      <div class="form-grid">
        <div class="input">Name</div><div class="input">Email</div>
        <div class="input">Phone</div><div class="input">Subject</div>
        <div class="input textarea">Message</div>
        <a class="submit" href="#">SUBMIT</a>
      </div>
    </div>
  </div>
</footer>

<div class="copyright">
  <div class="wrap">Copyright © 2015 Skyward Lens Reels. All Rights Reserved.<br>Terms &amp; Conditions | Privacy Policy | Terms of Use</div>
</div>

</body>
</html>
```